Recycling Exhibition Web Design Project

We are developing a new website for a exhibition we have just taken over. The previous site is very basic and we require a complete redesign. The site should be designed to engage with and attract those who work in or provide services to the multibillion dollar wastes and recycling industry in the Asia pacific region. These will include Federal & State Governments, City councils, private sector, industry associations and other key bodies, education facilities.

KTLO is the premier waste and recycling event in the Asia Pacific region and known as place where the industry meets to share innovations, gain knowledge, to network and do business.
• Innovation
• Knowledge transfer
• Industry Networking
• Trade
Key point: need to reflect that 2012 show will attract large numbers of quality visitors from across wide range of the industry – city councils, facilities managers, etc

Site should deliver 3 key objectives.
1. Stimulate interest those who work in or provide services to the wastes and recycling industry by providing simple to access, relevant and topical information about the Expo, the Seminars, the Key Features, the sub activities and the key benefits to them.
2. Provide a platform that supports / improves EP by providing a range of interactive components – ie floor plan / video. In addition options for sales enquiries, registration, general feedback
3. Provide a way to highlight / showcase sponsors, show features and other key assets. (possibly a carousel above the fold)

We really like the dunmar website so a take on this could be good (http://www.dunmar-example.com.au/). Also we want to try to reinforce the brand so we should use the event as the hero image/banner.

Previous website - http://www.ktlo-example.com.au/

Target Market(s)

The site should be designed to engage with and attract those who work in or provide services to the multibillion dollar wastes and recycling industry

Industry/Entity Type

Recycling

Requirements
Must have
• The icons on the current site work quite well so inclusion as CTAs would be preferable.

Other key areas are

• Seminar Delegate & Visitor Registration
• Exhibitor Prospectus
• Floorplan
• Conference / Seminar content
• Social media + blog

Site visitors will need to feel like they are part of a community.
Site should reflect/display key industry stats & stats from 2011 expo

Please see the attached brief for more details and site map for menu items.

```html
<!DOCTYPE html>
<html lang="en">
<head>
<meta charset="utf-8">
<title>KTLO Expo</title>
<link href="https://fonts.googleapis.com/css2?family=Source+Sans+3:wght@400;600;700&display=swap" rel="stylesheet">
<style>
:root{
  --page:#353535;
  --page-dark:#2b2b2b;
  --panel:#f1f1f1;
  --text:#3b3b3b;
  --red:#b0322a;
  --red-dark:#9c2a23;
  --orange:#e0652a;
  --amber:#f08a24;
  --green:#5e8a2a;
  --lime:#a9c23a;
  --white:#ffffff;
  --muted:#c9c9c9;
  --rule:#8a8a8a;
}
*{box-sizing:border-box;margin:0;padding:0}
html,body{width:883px;height:1200px;overflow:hidden}
body{background:linear-gradient(180deg,var(--page-dark),var(--page) 20%,var(--page));font-family:"Source Sans 3",Arial,sans-serif;color:var(--text);position:relative}
.abs{position:absolute}
.calendar-btn{left:711px;top:6px;width:118px;height:22px;background:#222;border-radius:0 0 3px 3px;color:#ddd;font-size:10px;display:flex;align-items:center;gap:7px;padding-left:17px}
.calendar-btn i{width:11px;height:11px;background:var(--orange);display:block;border-radius:1px}
.brand{left:40px;top:44px;display:flex;align-items:center;gap:10px;color:var(--white);font-size:34px;font-weight:700;letter-spacing:-.5px}
.brand i{width:28px;height:28px;border-radius:50%;background:var(--orange);display:block}
.tagline{left:500px;top:53px;width:218px;text-align:center;color:#ddd;font-size:10.5px;line-height:15px}
.nav{left:206px;top:92px;width:643px;height:37px;display:flex}
.nav a{flex:none;color:#eee;text-decoration:none;font-size:12.5px;display:flex;justify-content:center;padding-top:9px;border-bottom:4px solid}
.nav .active{background:var(--green);color:#fff}
.dropdown{left:566px;top:138px;width:144px;height:47px;background:var(--green);color:#fff;font-size:10px;line-height:14px;padding:8px 0 0 13px}
.content{left:34px;top:128px;width:815px;height:1005px;background:var(--panel)}
.hero{left:60px;top:142px;width:764px;height:262px;background:radial-gradient(circle at 560px 95px,#b9c2c8 0,#6b7178 60px,#202020 130px,#0d0d0d 320px)}
.hero-text{left:148px;top:228px;color:#eee;font-size:17px;line-height:23px}
.arrow-btn{width:37px;height:34px;background:#555;border:1px solid #777;display:flex;align-items:center;justify-content:center}
.icon-bar{left:187px;top:362px;width:509px;height:72px;background:rgba(120,120,120,.55);display:flex}
.icon-bar div{flex:1;display:flex;flex-direction:column;align-items:center;padding-top:6px;color:#fff;font-size:8px;font-weight:700;line-height:8.5px;text-align:center}
.icon-bar div:nth-child(n){}
.icon-labels{left:187px;top:410px;width:509px;height:24px;background:#c4c4c4}
h1{left:42px;top:448px;color:var(--red);font-size:21px;font-weight:400}
h2{left:42px;top:483px;color:var(--orange);font-size:13px;font-weight:400}
.quotes{left:43px;top:510px;width:464px;font-size:10.5px;line-height:15px}
.quotes p{margin-bottom:14px}
.quotes b{font-weight:400;color:#111;display:block}
.video{left:519px;top:475px;width:317px;height:180px;background:#ddd;border:1px solid #bbb;padding:2px}
.video .frame{width:100%;height:100%;background:linear-gradient(180deg,#2a2a2a,#6a6a62 55%,#1e1e1e)}
.presenters{left:41px;top:683px;width:462px;height:308px;background:var(--red)}
.presenters h3{position:absolute;left:10px;top:9px;color:#fff;font-size:15px;font-weight:600}
.card{width:215px;height:127px;background:#fff;position:absolute}
.card .photo{position:absolute;left:2px;top:2px;width:98px;height:123px}
.card .name{position:absolute;left:108px;top:16px;color:var(--red);font-size:11px;font-weight:700}
.card .role{position:absolute;left:108px;top:35px;font-size:9.5px;line-height:12px;color:#333}
.stats{left:520px;top:684px;width:314px;font-size:10.5px;line-height:15px}
.stats h4{color:var(--red);font-size:10.5px;font-weight:400;margin-bottom:7px}
.stats section{border-bottom:1px dotted var(--rule);padding-bottom:7px;margin-bottom:14px}
.partners-title{left:42px;top:1016px;color:var(--red);font-size:14px}
.partners-rule{left:42px;top:1046px;width:800px;height:1px;background:#ccc}
.partner{color:var(--red-dark);font-size:13px;line-height:14px}
.footer-links{left:43px;top:1152px;color:#ddd;font-size:10px}
.copyright{left:43px;top:1175px;color:#ddd;font-size:10px}
.social{top:1160px;width:20px;height:20px;background:#4a6ea8;border-radius:2px}
</style>
</head>
<body>
<div class="abs calendar-btn"><i></i>Add to Calender</div>
<div class="abs brand"><i></i>KTLO Expo</div>
<div class="abs tagline">Exhibiting information, exhibtior profile and the links to key website content.</div>

<nav class="abs nav">
  <a style="width:63px;border-color:var(--red)">Home</a>
  <a style="width:108px;border-color:var(--red)">About the Show</a>
  <a style="width:94px;border-color:var(--amber)">What's on</a>
  <a style="width:95px;border-color:var(--green)">Register</a>
  <a class="active" style="width:94px;border-color:var(--green)">How to Exhibit</a>
  <a style="width:92px;border-color:var(--lime)">Blog</a>
  <a style="width:97px;border-color:var(--red)">Contact Us</a>
</nav>

<div class="abs content"></div>
<div class="abs hero" role="img" aria-label="Hero banner photo: child looking through a recycling bin opening holding fruit scraps"></div>
<div class="abs dropdown">• Post Show Report<br>&nbsp;&nbsp;Key statistics about the show</div>
<div class="abs hero-text">Want to know what is next in waste,<br>recycling and sustainability?</div>
<div class="abs arrow-btn" style="left:89px;top:257px"><svg width="10" height="14"><path d="M8 1 2 7l6 6" stroke="#fff" stroke-width="2.5" fill="none"/></svg></div>
<div class="abs arrow-btn" style="left:755px;top:257px"><svg width="10" height="14"><path d="M2 1l6 6-6 6" stroke="#fff" stroke-width="2.5" fill="none"/></svg></div>

<div class="abs icon-labels"></div>
<div class="abs icon-bar">
  <div><svg width="34" height="34"><path d="M17 3 32 30H2z" fill="none" stroke="#fff" stroke-width="3"/></svg><span style="color:#222;margin-top:5px">HAZARDOUS<br>WASTE</span></div>
  <div><svg width="34" height="34"><rect x="6" y="8" width="22" height="18" fill="none" stroke="#fff" stroke-width="3" transform="rotate(-25 17 17)"/></svg><span style="color:#222;margin-top:5px">DISPOSAL</span></div>
  <div><svg width="34" height="34"><circle cx="17" cy="17" r="11" fill="none" stroke="#fff" stroke-width="3"/><path d="M6 20h22" stroke="#fff" stroke-width="3"/></svg><span style="color:#222;margin-top:5px">COMPOST</span></div>
  <div><svg width="34" height="34"><circle cx="17" cy="13" r="9" fill="none" stroke="#fff" stroke-width="3"/><rect x="13" y="23" width="8" height="7" fill="#fff"/></svg><span style="color:#222;margin-top:5px">ENERGY<br>FROM WASTE</span></div>
  <div><svg width="34" height="34"><path d="M8 8h18l-2 23H10z" fill="none" stroke="#fff" stroke-width="3"/><path d="M6 6h22" stroke="#fff" stroke-width="3"/></svg><span style="color:#222;margin-top:5px">BIN LINERS<br>&amp; CONTAINERS</span></div>
  <div><svg width="34" height="34"><path d="M10 6h8l4 7-4 7h-8l-4-7zM20 14h7l3 6-3 6h-7l-3-6z" fill="#fff"/></svg><span style="color:#222;margin-top:5px">MACHINERY<br>&amp; EQUIPMENT</span></div>
  <div><svg width="34" height="34"><path d="M3 7q7-3 14 1 7-4 14-1v22q-7-3-14 1-7-4-14-1z" fill="#fff"/></svg><span style="color:#222;margin-top:5px">SERVICE<br>&amp; SOLUTIONS</span></div>
  <div><svg width="34" height="34"><rect x="2" y="9" width="20" height="15" fill="#fff"/><path d="M22 13h7l4 5v6H22z" fill="#fff"/><circle cx="9" cy="27" r="3" fill="#fff"/><circle cx="27" cy="27" r="3" fill="#fff"/></svg><span style="color:#222;margin-top:5px">VEHICLES<br>&amp; PLANT</span></div>
  <div><svg width="34" height="34"><path d="M17 4l-6 10h12zM5 28l5-10 6 10zM29 28l-5-10-6 10z" fill="#fff"/></svg><span style="color:#222;margin-top:5px">RECYCLED<br>PRODUCTS</span></div>
</div>

<h1 class="abs">Welcome to our site</h1>
<h2 class="abs">What our &nbsp;exhibitors and delegates have to say....</h2>
<div class="abs quotes">
  <p>"KTLO was the perfect venue for us to launch our new organics units. In this digital era, being able to speak face-to-face and show visitors how the units work really helped them to understand the benefits. The quality and quantity of the visitors was just what we were looking for."<b>Circuit Cycle &nbsp;- 2011 Exhibitor.</b></p>
  <p>"I found our firm's participation in the 2011 KTLO conference rewarding given the opportunity to engage with colleagues and potential customers in the waste to energy industry. &nbsp;My attendance has led to business leads and to continued exposure to government and private sector &nbsp;interests in other venues."<b>Northbank Energy Recovery Pty Ltd - 2011 Delegate.</b></p>
</div>

<div class="abs video">
  <div class="frame" role="img" aria-label="Video still of the expo registration area"></div>
  <svg class="abs" style="left:137px;top:72px" width="40" height="40"><circle cx="20" cy="20" r="19" fill="rgba(0,0,0,.55)"/><path d="M15 11l13 9-13 9z" fill="#fff"/></svg>
  <div class="abs" style="left:2px;top:160px;width:311px;height:16px;background:#111;color:#ddd;font-size:8px;display:flex;align-items:center;gap:8px;padding:0 6px">
    <span>▶</span><span style="flex:1;height:3px;background:#555"></span><span>02:52</span><span>360p</span>
  </div>
  <span class="abs" style="left:32px;top:152px;font-size:7px;color:#fff;background:#111;padding:0 2px">0:00</span>
</div>

<div class="abs presenters">
  <h3>Conference Presenters</h3>
  <svg class="abs" style="left:420px;top:12px" width="34" height="14"><path d="M9 2 4 7l5 5M25 2l5 5-5 5" stroke="#fff" stroke-width="2.5" fill="none"/></svg>
  <div class="card" style="left:9px;top:37px"><div class="photo" role="img" aria-label="Portrait of presenter" style="background:linear-gradient(#7b6a5c,#2a2d3a)"></div><div class="name">Rob Ellery MP</div><div class="role">Federal Member<br>for Tarwin</div></div>
  <div class="card" style="left:237px;top:37px"><div class="photo" role="img" aria-label="Portrait of presenter" style="background:linear-gradient(#3d5a2a,#1c2418)"></div><div class="name">Cr Gena Marlow</div><div class="role">President CLGA &amp; Mayor<br>Harbourside Council</div></div>
  <div class="card" style="left:9px;top:172px"><div class="photo" role="img" aria-label="Portrait of presenter" style="background:linear-gradient(#4f6050,#6b6e6f)"></div><div class="name">Rob Ellery MP</div><div class="role">Federal Member<br>for Tarwin</div></div>
  <div class="card" style="left:237px;top:172px"><div class="photo" role="img" aria-label="Portrait of presenter" style="background:linear-gradient(#6b86a8,#252a38)"></div><div class="name">Cr Gena Marlow</div><div class="role">President CLGA &amp; Mayor<br>Harbourside Council</div></div>
</div>

<div class="abs stats">
  <section><h4>Trade show</h4>95 exhibitors from the U.S, U.K, NZ &amp; Australia filled Hall 5 at the Harbour Convention &amp; Exhibition Centre.</section>
  <section><h4>Full conference</h4>Rob Ellery, MP delivered the keynote address. More than 350 professionals registered for one or more of the four half day conference sessions.</section>
  <section><h4>Free workshops</h4>Over 120 people enjoyed one of the free workshops held.</section>
  <section><h4>Networking functions</h4>Networking functions<br>The Hon. Robyn Hale, MP &nbsp;opened the networking function attended by 400 sustainability professionals.</section>
</div>

<div class="abs partners-title">Media Partners</div>
<svg class="abs" style="left:797px;top:1019px" width="34" height="14"><path d="M9 2 4 7l5 5M25 2l5 5-5 5" stroke="var(--red)" stroke-width="2.5" fill="none"/></svg>
<div class="abs partners-rule"></div>
<div class="abs partner" style="left:42px;top:1068px">Regional Councils<br>Association</div>
<div class="abs partner" style="left:160px;top:1068px;display:flex;gap:8px;align-items:center"><i style="width:30px;height:30px;background:#b9a6a0;display:block"></i>Shires<br>Network</div>
<div class="abs partner" style="left:334px;top:1064px;font-size:26px;line-height:28px">WRMA</div>
<div class="abs partner" style="left:544px;top:1062px;font-size:24px;line-height:28px">Coverflex</div>
<div class="abs" style="left:758px;top:1062px;width:34px;height:34px;border-radius:50%;background:#c9a6a4"></div>

<div class="abs footer-links">Home &nbsp;| &nbsp;About the Show &nbsp;| &nbsp;What's on &nbsp;| &nbsp;Register &nbsp;| &nbsp;How to Exhibit &nbsp;| &nbsp;Blog &nbsp;| &nbsp;Contact Us &nbsp;| &nbsp;Sitemap</div>
<div class="abs copyright">Copyright © 2012 www.ktlo-example.com &nbsp;All rights reserved</div>
<div class="abs social" style="left:758px"></div>
<div class="abs social" style="left:789px;background:#3c8fc4"></div>
<div class="abs social" style="left:820px;background:#2f6e9c"></div>
</body>
</html>
```